Amber Reed Properties, which offers a selection of prime properties (villas

A website that contains: Idea, benefits, destinations (villas), offers, about us, contact, newsletter, social media, blog, look at the attachment, even if it is in German. The idea is that I can easily add new pages, if necessary, with the design you make. Later on we want to add a reservation system, so you can book your villa through the internet. Besides, there is a concierge service available, which organizes everything for the customer, owner, from villa to restaurant, limo service, ... & benefits and emotions through nice pictures / videos, they should be convinced to invest.

Target Market(s)

Investors (golfer and non-golfer) which have 300'000 to invest in a kind of real-estate investing club

Number of Pages Required

5+ page

Font styles to use
Sans Serif

Requirements
Must have
• It must be for wordpress, must have an exclusive touch, high quality, with nice pictures of golf courses. The Logo is gold so it has to match with gold, the font is segan or segoe semilight or similar, sans serif
Nice to have
• may be as well as the possibility to include videos of the different destinations and houses

```html
<!DOCTYPE html>
<html lang="de">
<head>
<meta charset="utf-8">
<title>Amber Reed Properties</title>
<link rel="stylesheet" href="https://fonts.googleapis.com/css2?family=Open+Sans:wght@300;400;600;700&display=swap">
<style>
:root{
  --gold:#e8a317;
  --gold-dark:#c98a0e;
  --ink:#2d2d2d;
  --text:#555;
  --muted:#8a8a8a;
  --navy:#1e3346;
  --footer:#3a3a3a;
  --footer-dark:#2c2c2c;
  --white:#fff;
}
*{box-sizing:border-box;margin:0;padding:0}
html,body{width:1200px;height:4672px;overflow:hidden;background:var(--white)}
body{position:relative;font-family:"Open Sans",Arial,sans-serif;color:var(--text)}
.abs{position:absolute}
.photo{position:absolute}

/* header */
.nav{position:absolute;left:0;top:0;width:1200px;height:64px;background:rgba(20,20,20,.55);z-index:5}
.nav a{position:absolute;top:22px;color:var(--white);font-size:15px;font-weight:600;text-decoration:none;letter-spacing:.5px}
.logo-plate{position:absolute;left:470px;top:0;width:260px;height:180px;z-index:6}
.logo-name{position:absolute;left:470px;top:98px;width:260px;text-align:center;color:var(--gold);font-size:14px;font-weight:700;letter-spacing:.5px;white-space:nowrap;z-index:7}
.logo-mark{position:absolute;left:586px;top:56px;width:28px;height:24px;border:3px solid var(--gold);z-index:7}

/* hero */
.hero-photo{left:0;top:0;width:1200px;height:840px;background:linear-gradient(180deg,#7e8f9c 0%,#a6b3bc 30%,#5b5e5c 55%,#2f3a3f 72%,#3c6f86 85%,#25485a 100%)}
.hero-title{position:absolute;top:296px;width:1200px;text-align:center;color:var(--white);font-size:60px;font-weight:700;letter-spacing:2px}
.hero-sub{position:absolute;top:388px;width:1200px;text-align:center;color:var(--white);font-size:24px;line-height:36px}
.dots{position:absolute;top:572px;left:560px;display:flex;gap:8px}
.dots span{width:14px;height:14px;border-radius:50%;background:rgba(255,255,255,.6)}
.dots span:first-child{background:var(--white)}

/* section headings */
.eyebrow{font-size:15px;font-weight:600;color:var(--ink);letter-spacing:.5px}
.heading{font-size:44px;font-weight:600;color:var(--gold);letter-spacing:1px;line-height:1.1}
.btn{display:inline-block;padding:12px 22px;font-size:15px;font-weight:600;color:var(--white);background:var(--gold)}
.btn.dark{background:#3a3a3a}

/* idea */
.idea-circle{left:110px;top:750px;width:300px;height:300px;border-radius:50%;border:10px solid #dfe6ea;background:linear-gradient(160deg,#6fa6d8 0%,#cfe0ee 45%,#f2f2ef 60%,#6f8a58 85%)}
.person{width:140px;height:140px;border-radius:50%;background:linear-gradient(180deg,#d9dde2,#6c7480);border:4px solid #eee}
.person-name{position:absolute;width:220px;text-align:center;font-size:15px;color:var(--ink);top:1236px}
.idea-head{right:120px;top:740px;text-align:right}
.idea-text{right:120px;top:846px;width:640px;text-align:right;font-size:15px;line-height:28px}
.idea-list{right:120px;top:1002px;text-align:right;font-size:15px;line-height:28px;color:var(--ink)}

/* benefits */
.benefits-photo{left:0;top:1320px;width:1200px;height:700px}
.benefits-head{left:110px;top:1484px;color:var(--white)}
.benefits-head .eyebrow{color:var(--white)}
.benefits-head .heading{color:var(--white);font-size:50px}
.ribbon{left:110px;top:1608px;height:46px;padding:0 28px 0 48px;background:#222;color:var(--white);font-size:22px;font-weight:600;line-height:46px}
.ribbon svg{position:absolute;left:14px;top:11px}
.benefit-text{left:110px;width:560px;color:var(--white);font-size:14px;line-height:24px}
.benefit-text li{list-style:none;padding-left:18px;position:relative}
.benefit-text li::before{content:"";position:absolute;left:2px;top:10px;width:6px;height:6px;background:var(--white);border-radius:50%}
.benefit-circle{left:750px;top:1530px;width:240px;height:240px;border-radius:50%;border:12px solid rgba(255,255,255,.7);background:radial-gradient(circle at 45% 40%,#55794b,#2c3f2a 70%)}

/* destinations */
.dest-head{left:120px;top:2116px}
.arrows{display:flex;gap:10px}
.arrows svg{display:block}
.dest-photo{top:2240px;height:310px}
.caption{position:absolute;top:2568px;text-align:center;font-size:16px;font-weight:700;color:var(--ink)}

/* about / offers */
.split-block{left:0;top:2740px;width:1200px;height:600px}
.split-col{width:420px;color:var(--white)}
.split-col .eyebrow{color:var(--white)}
.split-col .heading{color:var(--white);font-size:46px}
.split-col p{font-size:14px;line-height:22px;margin-top:20px}
.split-col .more{margin-top:22px;font-size:14px;font-weight:700}
.badge{width:60px;height:60px;margin-bottom:18px}

/* blog */
.blog-head{right:120px;top:3466px;text-align:right}
.blog-card{top:3548px;width:312px}
.blog-photo{position:relative;width:312px;height:240px}
.blog-card h3{margin-top:30px;text-align:center;font-size:16px;font-weight:700;color:var(--ink)}
.blog-card .date{text-align:center;font-size:12px;color:var(--gold);margin-top:4px}
.blog-card p{text-align:center;font-size:14px;line-height:20px;margin-top:8px;color:var(--muted)}
.blog-card .btn{display:block;width:110px;margin:20px auto 0;text-align:center;font-size:14px;padding:10px 0}

/* footer */
.footer{left:0;top:4120px;width:1200px;height:480px;background:var(--footer)}
.footer h4{font-size:34px;font-weight:400;color:var(--white);letter-spacing:1px}
.footer .rule{height:2px;background:#666;margin-top:16px;width:420px}
.contact-row{display:flex;align-items:flex-start;gap:18px;margin-top:26px;color:#ddd;font-size:14px;line-height:22px}
.icon-dot{flex:none;width:32px;height:32px;border-radius:50%;border:2px solid #aaa;display:flex;align-items:center;justify-content:center}
.email-field{margin-top:34px;width:420px;height:44px;border:1px solid #888;background:#333;color:#bbb;font-size:14px;padding:12px 14px}
.social{display:flex;gap:12px;margin-top:30px}
.social span{width:38px;height:38px;border-radius:50%;border:2px solid #aaa}
.copyright{left:0;top:4600px;width:1200px;height:72px;background:var(--footer-dark);color:#bbb;font-size:13px;text-align:center;line-height:72px}
.copyright .lang{position:absolute;right:40px;top:0}
</style>
</head>
<body>

<!-- HEADER -->
<nav class="nav">
  <a style="left:110px">HOME</a>
  <a style="left:186px">BENEFITS</a>
  <a style="left:286px">DESTINATIONS</a>
  <a style="left:800px">OFFERS</a>
  <a style="left:884px">ABOUT US</a>
  <a style="left:990px">CONTACT US</a>
</nav>
<svg class="logo-plate" viewBox="0 0 260 180"><path d="M0 0H260V40A130 140 0 0 1 0 40Z" fill="#1b1b1b" stroke="#e8a317" stroke-width="4"/></svg>
<div class="logo-mark"></div>
<div class="logo-name">AMBER REED PROPERTIES</div>

<!-- HERO -->
<div class="photo hero-photo" role="img" aria-label="Modern golf villa with pool at dusk"></div>
<svg class="abs" style="left:0;top:640px" width="1200" height="220" viewBox="0 0 1200 220">
  <path d="M0 60Q600 240 1200 60V220H0Z" fill="#fff"/>
  <path d="M0 60Q600 240 1200 60" fill="none" stroke="#e8a317" stroke-width="6"/>
</svg>
<h1 class="hero-title">AMBER REED PROPERTIES</h1>
<p class="hero-sub">A selection of prestige golf homes<br>to invest and enjoy</p>
<div class="dots"><span></span><span></span><span></span><span></span><span></span></div>

<!-- IDEA -->
<section>
  <div class="photo idea-circle" role="img" aria-label="White villa beside a golf course"></div>
  <div class="photo person" style="left:120px;top:1060px" role="img" aria-label="Portrait of partner Jonas F. Brenner"></div>
  <div class="photo person" style="left:300px;top:1060px" role="img" aria-label="Portrait of partner Lukas Hartwig"></div>
  <div class="person-name" style="left:80px">Jonas F. Brenner</div>
  <div class="person-name" style="left:260px">Lukas Hartwig</div>

  <div class="abs idea-head">
    <div class="eyebrow">AMBER REED PROPERTIES</div>
    <div class="heading">UNSERE IDEE</div>
  </div>
  <p class="abs idea-text">
    Wir bringen Immobilien-Investment, Golf und Lifestyle zusammen.<br>
    Die Idee folgt dem Wunsch nach Ruhe, Abwechslung und Genuss<br>
    auf höchstem Niveau und zu attraktiven Konditionen.<br>
    Das Konzept entstand im Gespräch unter Golffreunden.<br>
    Exklusive Villen an den schönsten Plätzen Europas.
  </p>
  <ul class="abs idea-list" style="list-style:none">
    <li>Ruhe</li>
    <li>Golfplätze Partnerschaft</li>
    <li>Sicherheit</li>
    <li>Resort-Infrastruktur &amp; Service</li>
    <li>Werterhaltung</li>
  </ul>
  <a class="abs btn" style="right:120px;top:1164px">Read More</a>
</section>

<!-- BENEFITS -->
<section>
  <svg class="photo benefits-photo" viewBox="0 0 1200 700" role="img" aria-label="Golden-toned resort and golf landscape">
    <defs>
      <linearGradient id="benefitsTone" x1="0" y1="0" x2="1" y2="1">
        <stop offset="0" stop-color="#c98a0e"/><stop offset=".5" stop-color="#e2a52a"/><stop offset="1" stop-color="#b97e12"/>
      </linearGradient>
    </defs>
    <path d="M0 10Q600 -50 1200 60V640Q600 760 0 650Z" fill="url(#benefitsTone)"/>
    <path d="M0 10Q600 -50 1200 60" fill="none" stroke="#fff" stroke-width="4" opacity=".7"/>
    <path d="M1200 640Q600 760 0 650" fill="none" stroke="#fff" stroke-width="4" opacity=".7"/>
  </svg>
  <div class="abs benefits-head">
    <div class="eyebrow">AMBER REED PROPERTIES</div>
    <div class="heading">BENEFITS</div>
  </div>
  <div class="abs ribbon">
    <svg width="22" height="24" viewBox="0 0 22 24"><path d="M16 2L6 12L16 22" fill="none" stroke="#e8a317" stroke-width="4"/></svg>
    Ihr Nutzen – Emotional
  </div>
  <ul class="abs benefit-text" style="top:1676px">
    <li>Sie sind Mitglied einer exklusiven Gemeinschaft von Investoren in traumhaften Golfdestinationen mit persönlicher Betreuung.</li>
    <li>Genießen Sie Ihre Villa, wann immer Sie möchten.</li>
  </ul>
  <ul class="abs benefit-text" style="top:1810px">
    <li>Sie gewinnen:<br>Erholung, Sonne und Golf an erstklassigen Plätzen, dazu Zugang zu Restaurants, Concierge und Limousinenservice.<br>Ruhe und Wertanlage.</li>
  </ul>
  <div class="photo benefit-circle" role="img" aria-label="Golf green framed in a round lens"></div>
</section>

<!-- DESTINATIONS -->
<section>
  <div class="abs dest-head">
    <div class="eyebrow">AMBER REED PROPERTIES</div>
    <div class="heading">DESTINATIONS</div>
  </div>
  <div class="abs arrows" style="left:1016px;top:2120px">
    <svg width="24" height="40" viewBox="0 0 24 40"><path d="M20 4L4 20L20 36" fill="none" stroke="#ccc" stroke-width="3"/></svg>
    <svg width="24" height="40" viewBox="0 0 24 40"><path d="M4 4L20 20L4 36" fill="none" stroke="#333" stroke-width="3"/></svg>
  </div>
  <div class="photo dest-photo" style="left:120px;width:300px;background:linear-gradient(180deg,#3f8fd6,#bcd7ee 45%,#f4f4f2 60%,#4bb3d8 80%,#7b9e5a)" role="img" aria-label="Villa with pool in Sierra Verde, Alicante"></div>
  <div class="photo dest-photo" style="left:442px;width:310px;background:linear-gradient(180deg,#9ac0dd,#e9e6df 40%,#5c8a4a 65%,#39a6d4 85%)" role="img" aria-label="Resort villa in Costa Alta, Tenerife"></div>
  <div class="photo dest-photo" style="left:772px;width:308px;background:linear-gradient(180deg,#2f84d1,#9ccaf0 35%,#e9d8b4 55%,#4ab8e6 78%,#3a7fb0)" role="img" aria-label="Villa and pool in Quinta do Mar, Algarve"></div>
  <div class="caption" style="left:120px;width:300px">SIERRA VERDE, ALICANTE</div>
  <div class="caption" style="left:442px;width:310px">COSTA ALTA, TENERIFFA</div>
  <div class="caption" style="left:772px;width:308px">QUINTA DO MAR, ALGARVE</div>
</section>

<!-- ABOUT / OFFERS -->
<section>
  <svg class="photo split-block" viewBox="0 0 1200 600" role="img" aria-label="Villa exterior at night in navy and gold tones">
    <defs>
      <clipPath id="lens"><path d="M0 80Q600 -60 1200 80V520Q600 660 0 520Z"/></clipPath>
      <linearGradient id="navyTone" x1="0" y1="0" x2="0" y2="1"><stop offset="0" stop-color="#2b4660"/><stop offset="1" stop-color="#15263a"/></linearGradient>
      <linearGradient id="goldTone" x1="0" y1="0" x2="0" y2="1"><stop offset="0" stop-color="#e7a526"/><stop offset="1" stop-color="#c68a12"/></linearGradient>
    </defs>
    <g clip-path="url(#lens)">
      <rect x="0" y="0" width="600" height="600" fill="url(#navyTone)"/>
      <rect x="600" y="0" width="600" height="600" fill="url(#goldTone)"/>
    </g>
    <path d="M0 80Q600 -60 1200 80" fill="none" stroke="#c9d3dc" stroke-width="4"/>
    <path d="M0 520Q600 660 1200 520" fill="none" stroke="#c9d3dc" stroke-width="4"/>
  </svg>
  <div class="abs split-col" style="left:120px;top:2864px">
    <svg class="badge" viewBox="0 0 60 60"><path d="M8 26L30 10L52 26M14 24V50H46V24M24 50V36H36V50" fill="none" stroke="#fff" stroke-width="3"/></svg>
    <div class="eyebrow">AMBER REED PROPERTIES</div>
    <div class="heading">ABOUT US</div>
    <p>Wir sind ein kleines Team aus Golfern und Immobilienexperten, das Investoren exklusive Villen in den schönsten Golfregionen Europas eröffnet.</p>
    <div class="more">Read More →</div>
  </div>
  <div class="abs split-col" style="left:660px;top:2864px">
    <svg class="badge" viewBox="0 0 60 60"><circle cx="30" cy="30" r="26" fill="none" stroke="#fff" stroke-width="3"/><path d="M20 40L40 20" stroke="#fff" stroke-width="3"/><circle cx="22" cy="22" r="4" fill="#fff"/><circle cx="38" cy="38" r="4" fill="#fff"/></svg>
    <div class="eyebrow">AMBER REED PROPERTIES</div>
    <div class="heading">OFFERS</div>
    <p>Aktuelle Angebote für Villen und Beteiligungen mit Concierge-Service, Reservierung und Betreuung vor Ort, sorgfältig für Sie ausgewählt.</p>
    <div class="more">Read More →</div>
  </div>
</section>

<!-- BLOG -->
<section>
  <div class="abs arrows" style="left:110px;top:3444px">
    <svg width="24" height="40" viewBox="0 0 24 40"><path d="M20 4L4 20L20 36" fill="none" stroke="#333" stroke-width="3"/></svg>
    <svg width="24" height="40" viewBox="0 0 24 40"><path d="M4 4L20 20L4 36" fill="none" stroke="#ccc" stroke-width="3"/></svg>
  </div>
  <div class="abs blog-head">
    <div class="eyebrow">AMBER REED PROPERTIES</div>
    <div class="heading">BLOG POSTS</div>
  </div>
  <article class="abs blog-card" style="left:110px">
    <div class="blog-photo" style="background:linear-gradient(180deg,#4a93d4,#cfe1f0 45%,#f3f3f1 65%,#6e8f58)" role="img" aria-label="Modern white villa"></div>
    <h3>NEMO ENIM IPSAM</h3>
    <div class="date">MAY 12, 2016</div>
    <p>Neue Golfvillen an der Küste,<br>jetzt zur Besichtigung bereit.</p>
    <a class="btn dark">Read More</a>
  </article>
  <article class="abs blog-card" style="left:444px">
    <div class="blog-photo" style="background:linear-gradient(180deg,#8fb8da,#e7e3db 45%,#39a6d4 75%,#2d7fae)" role="img" aria-label="Villa terrace with pool"></div>
    <h3>SED UT PERSPICIATIS</h3>
    <div class="date">MAY 12, 2016</div>
    <p>Ein Wochenende auf dem Platz,<br>Tipps für Ihre nächste Runde.</p>
    <a class="btn">Read More</a>
  </article>
  <article class="abs blog-card" style="left:778px">
    <div class="blog-photo" style="background:linear-gradient(180deg,#6fa8dc,#f0d9c0 45%,#e6c9a8 65%,#4bb4e0)" role="img" aria-label="Mediterranean villa with pool"></div>
    <h3>NEQUE PORRO QUISQUAM</h3>
    <div class="date">MAY 12, 2016</div>
    <p>Concierge-Service vor Ort,<br>vom Restaurant bis zur Limousine.</p>
    <a class="btn dark">Read More</a>
  </article>
</section>

<!-- FOOTER -->
<footer class="abs footer">
  <div class="abs" style="left:120px;top:100px">
    <h4>CONTACT US</h4>
    <div class="rule"></div>
    <div class="contact-row">
      <span class="icon-dot"><svg width="14" height="16" viewBox="0 0 14 16"><path d="M7 15C3 10 1 7 1 5A6 6 0 0 1 13 5C13 7 11 10 7 15Z" fill="none" stroke="#ddd" stroke-width="1.6"/><circle cx="7" cy="5" r="2" fill="#ddd"/></svg></span>
      <span>c/o Fairway Estate Holding GmbH<br>Seestrasse 12, CH-8000 Zürich<br>Zürich / Switzerland</span>
    </div>
    <div class="contact-row">
      <span class="icon-dot"><svg width="14" height="14" viewBox="0 0 14 14"><path d="M3 1L5 4L4 6Q6 9 8 10L10 9L13 11L12 13Q6 13 1 3Z" fill="#ddd"/></svg></span>
      <span>+41 44 000 12 34<br>+41 79 000 56 78</span>
    </div>
    <div class="contact-row">
      <span class="icon-dot"><svg width="14" height="12" viewBox="0 0 14 12"><rect x="1" y="1" width="12" height="10" fill="none" stroke="#ddd" stroke-width="1.4"/><path d="M1 1L7 6L13 1" fill="none" stroke="#ddd" stroke-width="1.4"/></svg></span>
      <span>info@amberreed-example.ch</span>
    </div>
  </div>
  <div class="abs" style="left:660px;top:100px">
    <h4>NEWSLETTER</h4>
    <div class="rule"></div>
    <div class="email-field">Email Address</div>
    <a class="btn" style="margin-top:16px;font-size:13px;padding:10px 18px">SUBSCRIBE</a>
    <div class="social"><span></span><span></span><span></span><span></span><span></span><span></span></div>
  </div>
</footer>
<div class="abs copyright">Copyrights © 2016 Amber Reed Properties. All Rights Reserved.<span class="lang">DE</span></div>

</body>
</html>
```